Inspiration Poster

Inspirational Poster that has a Kamran Dulo like abstract look (http://www.vexalo.com/images/search?q=kamran+dulo&FORM=HDRSC2) with the text:

"we walk not in order to arrive at the promise land but because walking itself is a revolution"
-Peter Ambrick

```html
<!DOCTYPE html>
<html lang="en">
<head>
<meta charset="utf-8">
<title>Inspiration Poster — Walking Itself Is a Revolution</title>
<link rel="stylesheet" href="https://fonts.googleapis.com/css2?family=Righteous&family=Roboto:wght@400&display=swap">
<style>
  :root {
    --page: #ffffff;
    --board-light: #cfcfcf;
    --board-mid: #a9a9a9;
    --board-dark: #5e5e5e;
    --seam: #4a4a4a;
    --lime: #a6f21c;
    --ink: #1a1a1a;
    --shadow: rgba(70, 70, 70, 0.55);
  }
  * { margin: 0; padding: 0; box-sizing: border-box; }
  html, body {
    width: 848px; height: 1200px; overflow: hidden;
    background: var(--page);
  }
  .canvas { position: relative; width: 848px; height: 1200px; background: var(--page); }
  .poster {
    position: absolute; left: 70px; top: 70px; width: 708px; height: 1060px;
    overflow: hidden;
    background:
      linear-gradient(180deg, var(--board-mid) 0%, var(--board-light) 18%, var(--board-mid) 30%,
        var(--board-light) 45%, var(--board-mid) 62%, var(--board-light) 78%, var(--board-dark) 100%);
  }
  .poster-glow { position: absolute; inset: 0; }
  .tree-area {
    position: absolute; left: 115px; top: 350px; width: 580px; height: 720px;
    border-radius: 50% 50% 45% 45%;
    background: radial-gradient(ellipse 50% 50% at 50% 45%,
      rgba(25, 25, 25, 0.62) 0%,
      rgba(35, 35, 35, 0.45) 45%,
      rgba(60, 60, 60, 0.18) 75%,
      rgba(60, 60, 60, 0) 100%);
  }
  .quote { position: absolute; inset: 0; font-family: "Righteous", sans-serif; color: var(--ink); }
  .quote-line {
    position: absolute; white-space: nowrap; line-height: 1;
    text-shadow: 4px 5px 0 var(--shadow);
  }
  .line-we-walk { left: 57px; top: 40px; font-size: 46px; }
  .line-not-in-order { left: 150px; top: 88px; font-size: 36px; }
  .line-promise-land { left: 57px; top: 112px; font-size: 63px; }
  .line-but-because { left: 188px; top: 180px; font-size: 16px; text-shadow: 2px 3px 0 var(--shadow); }
  .line-walking-itself { left: 208px; top: 200px; font-size: 25px; }
  .line-revolution { left: 176px; top: 222px; font-size: 67px; }
  .attribution {
    position: absolute; left: 506px; top: 292px;
    font-family: "Roboto", sans-serif; font-style: normal; font-size: 18px; color: var(--ink);
    text-shadow: 2px 2px 0 var(--shadow);
  }
</style>
</head>
<body>
<div class="canvas">
  <div class="poster">
    <svg class="poster-glow" width="708" height="1060" viewBox="0 0 708 1060" aria-hidden="true">
      <defs>
        <radialGradient id="lime-wash">
          <stop offset="0" stop-color="#a6f21c" stop-opacity="0.95"/>
          <stop offset="0.6" stop-color="#a6f21c" stop-opacity="0.5"/>
          <stop offset="1" stop-color="#a6f21c" stop-opacity="0"/>
        </radialGradient>
      </defs>
      <ellipse cx="60" cy="220" rx="120" ry="160" fill="url(#lime-wash)"/>
      <ellipse cx="150" cy="540" rx="110" ry="190" fill="url(#lime-wash)"/>
      <ellipse cx="330" cy="660" rx="150" ry="120" fill="url(#lime-wash)"/>
      <ellipse cx="660" cy="590" rx="110" ry="150" fill="url(#lime-wash)"/>
      <ellipse cx="320" cy="40" rx="60" ry="40" fill="url(#lime-wash)"/>
      <line x1="0" y1="335" x2="708" y2="335" stroke="#4a4a4a" stroke-width="3"/>
      <line x1="0" y1="700" x2="708" y2="700" stroke="#4a4a4a" stroke-width="3"/>
    </svg>
    <div class="tree-area" role="img" aria-label="Silhouette of a bare winter tree with branching limbs against the textured board"></div>
    <blockquote class="quote">
      <span class="quote-line line-we-walk">"we walk</span>
      <span class="quote-line line-not-in-order">not in order to arrive at</span>
      <span class="quote-line line-promise-land">the promise land</span>
      <span class="quote-line line-but-because">but because</span>
      <span class="quote-line line-walking-itself">walking itself</span>
      <span class="quote-line line-revolution">is a revolution"</span>
    </blockquote>
    <cite class="attribution">Peter Ambrick</cite>
  </div>
</div>
</body>
</html>
```